Stem cell injections patient brochure

i need a patient brochure for stem cell injections

What started out as a controversial treatment option has turned out to be one of the most unique solutions when it comes to treating joint pain and other health conditions that require the rejuvenation or replacement of certain types of tissues. Individuals who have trouble with their joints due to damage to the bone and cartilage are eager to find solutions that do not involve surgery. Stem cell therapy and the use of amniotic fluids offer solutions that will allow them to begin the healing process and begin to reclaim their lives. Stem cells and the use of platelet rich plasma go hand in hand in helping to regenerate and restore joint structure and function allowing the person to regain their mobility without fear of creating more discomfort.

Uncovering the Benefits of Stem Cells

The study of stem cells has uncovered a myriad of benefits ranging from the relief of migraines to the restoration and rejuvenation of various joints throughout the body. Stem cells are harvested from the patient allowing for a more complete healing in which the body's own tools are given a boost to begin the rejuvenation process. Because the stem cells are drawn from the person's own body, there is less risk of rejection and the body will begin to restore itself much faster than if foreign cells were used. When it comes to the regeneration of tissues in the joints, stem cell therapy offers a unique approach that allows the body to use its own resources in the healing process. Stem cell therapy takes an existing process and gives it a dramatic boost that basically pushes the process into overdrive, regenerating damaged tissue and sustaining the healing response. One thing that many people like about the procedure is that the matrix used in the injections is made from stem cells, growth factors and platelets that are harvested from their own body. No foreign substances are used and the healing process that results is much more efficient and complete. The body is given exactly what it needs to heal itself on its own terms without toxic chemicals or invasive procedures that takes weeks or months to heal.

A Unique Treatment Solution

Stem cells offer treatment options and solutions that were unheard of as little as three decades ago. By injecting a matrix made from the body's own “blank” cells, the body is able to regenerate new, healthier tissues that grow and take the place of damaged tissues. Along with the blank, stem cells, certain growth factors are also harvested and added to the mix. Because of how stem cells are formed, they can begin to assume the DNA of almost any type of cell. This allows them to grow into whatever type of cell is needed, hastening the healing process by rebuilding stronger and healthier tissue. The body has been given the tools it needs to heal itself but it often has trouble setting the processes in motion. Stem cell therapy gives the body the boost it needs by flooding the area with the stem cells that can actually elicit a healing response and trigger the start of the process.

Where Do Stem Cells Come From?

Stem cells are no longer drawn from outside sources to be used in joint rejuvenation procedures. The body has an unlimited supply of stem cells that it uses on a regular basis as a way of replacing cells that mature and die off. Doctors have found ways to harvest those cells, as well as growth factors that help to hasten the healing process. Stem cells can be found throughout the entire body. They are produced in the bones, the blood, liver, brain, heart, and soft tissues. They can be found almost everywhere simply because they are the building blocks the body uses to maintain its structure. Because the body continually produces them, they can be harvested from almost any area at any time without fear of damaging existing tissues or disrupting other processes in the body.

What Types of Tissues Will Stem Cells Restore

Stems cells can be used to regenerate almost any type of tissue, including cartilage and bone. Most people who look to stem cell therapy, do so in the hopes that it will relieve their joint pain and allow the joint to function properly. Stem cells do have the capability of regenerating many different types of tissues, but their rate of effectiveness will be determined by existing factors, such as spurring, severe degeneration, and the presence of health conditions such as osteo- or rheumatoid arthritis. Each person's case is unique. The goal of the procedure is to regenerate the damaged tissues and reduce pain and discomfort. While the tissues may be regenerated and function partially restored, it may not provide enough of a change to completely eliminate all of the patient's pain or discomfort.

Stem Cell Treatment Options for Joints

Stem cell treatment options can be beneficial in many ways. They are fairly non-invasive in comparison to other types of procedures. The only part of the procedure that is termed as invasive would be the use of the needle to inject the matrix into the damaged area of the joint. There is practically no down-time and the patient can begin to resume their normal, day-to-day activities within a few hours after the procedure. While it may take a few weeks to begin to notice verifiable results, the addition of a platelet rich plasma injection a few weeks after the initial procedure will help to keep the healing process on track. When it comes to stem cell treatment options for knees and other joints, the procedure offers a unique solution that allows the body the opportunity to heal itself without harsh or extremely invasive procedures.

Is the Procedure Effective?

It has been proven that stem cells are capable of regenerating different types of tissues. The procedure's effectiveness, however, will be based on several factors. First and foremost, the extent of damage caused by the injury or disease will determine how effective the procedure will be. If the damage is extensive, the use of stem cells and platelet rich plasma injections may be beneficial, but it will not relieve all of the patient's pain and discomfort. The reason for this is that the damage may extend far beyond the cartilage and structural tissues. Nerves may be damaged or scar tissue may be present that limits how the bone and cartilage are able to heal. The patient's overall health will also play a vital role. Proper circulation and an abundance of oxygen and nutrients supplied by the bloodstream are imperative if the body's healing responses are expected to regenerate and restore the tissues. The person's willingness to follow the doctor's orders and maintain proper nutrition and sufficient amounts of physical therapy that is needed to strengthen the area are also important factors. In the first one or two months, patient will begin to notice less pain and discomfort. It can take up to six months or longer for the function to improve. The process will be gradual and will continue to improve over time.

Will More Injections be Needed in the Future?

In most cases, only one stem cell injection is used. To be effective, platelet rich plasma injections are included with the procedure so the stem cells continue to receive the nutrient's they need to continue the healing process. Platelet rich plasma is a matrix made up of approximately three times the number of platelets that are normally found in the blood. To make the PRP matrix, blood is drawn from the patients arm and concentrated to create a platelet rich solution that, when injected into an injured area, floods it with platelets that provide an abundance of nutrients that help to maintain the forward progress of the healing response. With one stem cell injection and one platelet rich plasma injection, spaced out over a period of three to four weeks, the patient will receive the maximum benefits from both procedures. Protocols can be adjusted if the person receiving the treatment is unavailable or needs to have the injections closer together.

How Do I Know if I Will Benefit From the Procedure?

Stem cell therapy is often considered for patients who have not responded well to other forms of treatment, especially for osteoarthritis. Individuals who have osteoarthritis may find it difficult to move the knee or other joint. They may also be experiencing reduced range of motion and flexibility which makes physical therapy difficult, not to mention, extremely painful. The longer the patient experiences impaired mobility, the harder it will be for them to remain active. Stem cell therapy may also be an effective option for individuals who would rather not go through the experience of a partial or total knee replacement procedure.

Individuals who have trouble with tendonitis caused by repetitive motions or movements due to a sport they participate in or as part of their work-related duties may be able to find the relief they seek by receiving stem cell and platelet rich plasma injections in the affected joints. Repetitive motions can damage both bone and cartilage causing inflammation and pain in and around the area of the joint. Over time, the pain and inflammation can become so severe that regular movement is difficult. Stem cell therapy can help to restore proper function by regenerating the damaged cartilage and tissues, much like it works within the knee joint. As the injured tissues begin to heal, the inflammation begins to decrease and the person will begin to experience greater range of motion and flexibility. Although stem cell injections may not completely correct the problem, it will help to reduce the pain and discomfort allowing the person freedom of movement and the ability to exercise the area and regain a portion of the strength that was lost.

Common Contraindications

Just like any other healthcare procedure, stem cell therapy does have several contraindications and is inadvisable for patients with specific health conditions. Individuals who have any type of blood borne cancer or have had cancer are normally encourage not to attempt a stem cell procedure. Leukemia and lymphoma are two cancers that are spread through the blood and can have a devastating impact on the body. Patients who are prone to any type of infection or have a depressed immune system should also avoid this type of procedure. The use of Velbrisol can also have a devastating impact on how the procedure works. Patients who use the drug on a regular basis are not good candidates for this type of procedure. Individuals who have chronic, recurring medical conditions that affect their general health and the body's ability to heal are also not good candidates.

Potential Risk Factors

Stem cell therapy has relatively few risks. The bone marrow cells are harvested from the patient's own tissues so there is minimal risk of rejection. The harvesting process may be somewhat uncomfortable but the doctor can offer medications to help alleviate any pain or discomfort. The cells are concentrated, separating the stem cells from other types of cells. Growth factors within the blood are allowed to remain in tact as a sort of booster that helps to kick start the process into motion. A mixture of highly concentrated stem cells and growth factors is created and injected directly into the affected area of the joint. Any injection will result in minimal amounts of pain. Doctors may offer a mild local anesthetic or they may prescribe a pain medication that can be taken after the procedure is over. Because the procedure is non-invasive, there is very little risk of infection and the healing time is relatively fast. The patient may experience mild pain and swelling near the injection site for the first few days after the procedure, but this will dissipate rather quickly allowing the person to return to their daily activities within a few hours.

The Procedure Itself

How Do I Prepare for the Procedure?

There is very little preparation needed before a stem cell injection procedure. Doctors recommend no anti-inflammatory medications for at least seven to ten days prior to the procedure. It is important to drink plenty of fluids prior to the procedure and make sure you are well rested and able to follow all of the doctor's requests once the procedure is underway. During your initial visit, the doctor will ask if you are taking any medications, such as Pondrexa or Velbrisol. If you are, the doctor will need to know so that he can tell you when to discontinue the medication prior to the procedure being performed. The day of the procedure make sure you have someone who can take you home and look after you for the first few hours after the procedure. You will need to make arrangements so that you can rest once you arrive home. Do not try and over do it or exceed your personal limitations. Even though this is not a surgical procedure, the doctor may recommend not eating for a few hours prior to the procedure to prevent nausea and an upset stomach while you are receiving the treatment.

What Happens When I Arrive?

The morning of the procedure make sure you are well rested and wearing comfortable clothes, You will be checked in and taken back to a room where the procedure will be performed. The nurse will prep the knee (or other joint) and make sure all of the tools are available for the doctor to use. The doctor will begin the harvesting process, which involves drawing blood and stem cells from the marrow of one of your bones. You will be allowed to rest while the matrix is being created. Once the stem cell solution has been created, the doctor will identify the area where the injection needs to be placed. The solution will then be injected into the joint.

What Are My Limitations After the Procedure?

Stem cell procedures do not produce immediate results. Although they will provide significant improvement when it comes to managing the patient's pain, the stem cells will not stimulate the growth of new cartilage over night. It can take anywhere from three to six months or longer for the patient to begin to experience noticeable results. The results may take even longer if the person has other health conditions that affect their body's ability to heal itself. Once the pain begins to subside, the patient should experience renewed mobility and range of motion that allow them to increase their flexibility and begin to exercise, even if only in modest amounts. The more the person moves the knees, strength will be improved. The more movement, the stronger the joint. As the healing process continues and more cartilage is regenerated, the fewer limitations the patient will experience.

Stem cell therapy is not a quick fix. The benefits of giving the body what it needs to restore itself and heal on its own without extensive surgery or potent medications offers many benefits. The lack of risk improves the chances of a more complete healing and allows the body to recover in a natural way that is more efficient and productive than if a surgery or other invasive procedure had been performed. The person's overall general health will determine the rate at which a person heals. Encouraging proper lifestyle habits, proper nutrition, adequate amounts of fluids and regular exercise will increase the patient's ability to heal faster and more effectively than someone who lives a sedentary lifestyle.

Talk to Your Doctor

Individuals who are experiencing knee or joint pain for any reason should consult with their doctor and ask whether or not stem cell therapy is right for them. Individuals who suffer from osteoarthritis and other types of degenerative bone condition may benefit substantially from a stem cell therapy procedure. Athletes who have repeatedly stressed or injured their joints may also be good candidates for this type of procedure. Common athletic injuries such as tendonitis can be effectively treated with a combination of stem cell therapy and platelet rich plasma injections. Repeated motion injuries like swimmer's shoulder, pitcher's elbow and carpal tunnel syndrome can be treated with stem cell injections when other treatment options begin to fail to produce sufficient relief. With these types of injuries, the regeneration of the tissues and cartilage not only significantly reduce the pain and discomfort a person feels when performing certain tasks, it also allows the person to regain the majority of their range of motion they may have otherwise lost.

It is important to remember that most insurance companies list this as an elective procedure so it is not normally covered under your health insurance. While it is recognized as an effective treatment by some, the protocols and benefits are still being researched. Studies are still being performed to provide accurate information on how effective the treatment is when used to treat specific types of injuries or illnesses. Until a consensus is reached and the NMB approves the procedure along with a list of conditions that it is capable of treating, insurance companies will not include coverage for this type of procedure in their health care policies.

If you have any questions or concerns about the cost of the procedure, how it is performed, the benefits, the risks, and whether or not there are any concerns or implications you need to be aware of, talk to your doctor. He will be able to offer advice and answer any of the questions you may have concerning the procedure. Your general health and lifestyle will determine whether or not the treatment is suitable for the issues you are having with your knees or other joints. Before you make the decision on whether or not to have the stem cell procedure performed, make sure you have all of the information you need to make a knowledgeable choice. Giving the body the tools it needs to heal itself using its own healing responses is beneficial in many ways, but it may not be the right option for you. Talk to your doctor and weigh both pros and cons before making your decision.

ient brochure trifold that explains stem cell injections

Target Market(s)

patient brochure

Industry/Entity Type

Health Care

Requirements
Must have
• dna pictures
• large trifold brochure
Nice to have
• stem cell pictures and injections

```html
<!DOCTYPE html>
<html lang="en">
<head>
<meta charset="utf-8">
<title>Restoration Through Stem Cell Therapy – Patient Brochure</title>
<link rel="stylesheet" href="https://fonts.googleapis.com/css2?family=Montserrat:wght@300;400;600;700&family=Open+Sans:wght@400&display=swap">
<style>
:root{
  --teal:#2cb6d1;
  --teal-deep:#2a8ca8;
  --teal-soft:#d9f1f6;
  --ink:#5c6670;
  --paper:#ffffff;
  --paper-grey:#eceef0;
  --stage:#e7e8ea;
  --heading-font:'Montserrat',sans-serif;
  --body-font:'Open Sans',sans-serif;
}
*{box-sizing:border-box;margin:0;padding:0}
html,body{width:1200px;height:1200px;overflow:hidden;background:var(--stage)}
.canvas{position:relative;width:1200px;height:1200px}
.panel{position:absolute;background:var(--paper);overflow:hidden;box-shadow:0 2px 8px rgba(0,0,0,.12)}
.h{font-family:var(--heading-font);font-weight:300;text-transform:uppercase;color:var(--teal);letter-spacing:.5px;line-height:1.1}
.h b{font-weight:700}
.h.light{color:#fff}
.copy{font-family:var(--body-font);font-size:6.6px;line-height:1.45;color:var(--ink);text-align:justify}
.copy.light{color:#eaf8fb}
.photo{position:absolute}

/* cover */
.cover{left:20px;top:20px;width:370px;height:560px}
.brand{position:absolute;left:26px;top:26px;display:flex;align-items:center;gap:8px;font-family:var(--heading-font);font-weight:600;font-size:20px;color:var(--teal-deep);letter-spacing:.5px}
.brand-square{width:18px;height:18px;background:var(--teal-deep)}
.cover .photo{left:0;top:70px;width:370px;height:290px;background:linear-gradient(135deg,#f5f8fb 0%,#dfe9f2 45%,#b9c9e0 100%)}
.cover-wave{position:absolute;left:0;top:280px;width:370px;height:130px}
.cover-band{position:absolute;left:0;top:340px;width:370px;height:110px;background:var(--teal);padding:26px 22px 0 0;text-align:right}
.cover-band .h{font-size:19px;color:#fff}
.cover-band .h b{font-size:21px}
.cover-sub{position:absolute;right:22px;top:480px;width:250px;text-align:right;font-family:var(--heading-font);font-size:10.5px;color:var(--ink);line-height:1.35}

/* inside middle panel */
.inside-mid{left:415px;top:20px;width:370px;height:560px}
.future{position:absolute;left:0;top:0;width:170px;height:330px;background:var(--teal);padding:20px 14px}
.future .h{font-size:12px;margin-bottom:8px}
.mid-col{position:absolute;left:182px;top:20px;width:176px}
.mid-col .h{font-size:12px;margin-bottom:6px}
.mid-col .copy{margin-bottom:12px}
.future-notch{position:absolute;left:170px;top:0;width:12px;height:330px}
.mid-left-lower{position:absolute;left:14px;top:345px;width:156px}
.inside-mid .photo{left:0;top:450px;width:370px;height:110px;background:linear-gradient(160deg,#f3dfe3 0%,#d9697b 50%,#a8233a 100%)}

/* procedure panel */
.procedure{left:810px;top:20px;width:370px;height:560px}
.procedure .photo{left:0;top:0;width:370px;height:120px;background:linear-gradient(120deg,#f2e3d6 0%,#d9b59a 55%,#c29679 100%)}
.procedure-bar{position:absolute;left:0;top:120px;width:290px;height:32px;background:var(--teal);padding:8px 16px}
.procedure-bar .h{font-size:14px;color:#fff}
.procedure-body{position:absolute;left:16px;top:166px;width:338px}
.procedure-body .h{font-size:11px;margin-bottom:5px}
.procedure-body .copy{margin-bottom:11px}

/* lower spread */
.spread-left{left:20px;top:610px;width:570px;height:570px;background:var(--paper-grey)}
.spread-right{left:610px;top:610px;width:570px;height:570px}
.intro{position:absolute;left:22px;top:20px;width:526px}
.intro .h{font-size:15px;margin-bottom:6px}
.intro .copy{margin-bottom:12px}
.unique{position:absolute;left:0;top:210px;width:300px;height:170px;background:var(--teal-deep);padding:16px 18px}
.unique .h{font-size:14px;margin-bottom:8px}
.spread-left .photo{left:300px;top:210px;width:270px;height:170px;background:linear-gradient(135deg,#f4f1ee 0%,#e8d6cc 45%,#c9ccd8 100%)}
.effective{position:absolute;left:0;top:380px;width:570px;height:190px;background:var(--paper);padding:18px 22px}
.effective .h{font-size:17px;margin-bottom:8px}

.spread-right .photo.cells{left:0;top:0;width:570px;height:150px;background:radial-gradient(circle at 30% 40%,#8fd6ef 0%,#3f9fd0 45%,#1d6aa6 100%)}
.where{position:absolute;left:0;top:150px;width:570px;height:215px;background:var(--paper);padding:16px 22px}
.where .h{font-size:16px;margin-bottom:6px}
.where .copy{margin-bottom:10px}
.joints{position:absolute;left:0;top:365px;width:570px;height:205px;background:var(--teal-deep)}
.joints .photo{left:0;top:0;width:200px;height:205px;background:linear-gradient(160deg,#bfe4f1 0%,#6fb4d3 55%,#3a86ad 100%)}
.joints-text{position:absolute;left:218px;top:16px;width:334px}
.joints-text .h{font-size:16px;margin-bottom:8px;color:#fff}
</style>
</head>
<body>
<main class="canvas">

  <!-- Front cover -->
  <section class="panel cover">
    <div class="brand"><span class="brand-square"></span>Restora Clinic</div>
    <div class="photo" role="img" aria-label="Photo of a lab technician with a pipette and test tubes"></div>
    <svg class="cover-wave" viewBox="0 0 370 130" preserveAspectRatio="none" aria-hidden="true">
      <path d="M0 70 C120 20 250 20 370 50 L370 130 L0 130 Z" fill="#bfe8f1" opacity=".7"/>
      <path d="M0 80 C120 40 250 40 370 60 L370 130 L0 130 Z" fill="#2cb6d1"/>
    </svg>
    <div class="cover-band">
      <h1 class="h">Restoration through<br><b>Stem cell therapy</b></h1>
    </div>
    <p class="cover-sub">A unique solution to treating joint pain and other health conditions without surgery</p>
  </section>

  <!-- Inside: future injections, contraindications, risk -->
  <section class="panel inside-mid">
    <div class="future">
      <h2 class="h light">Will more injections be needed <b>in the future?</b></h2>
      <p class="copy light">In most cases, only one stem cell injection is used. To be effective, platelet rich plasma injections are included with the procedure so the stem cells continue to receive the nutrients they need to continue the healing process. Platelet rich plasma is a matrix made up of approximately three times the number of platelets normally found in the blood. To make the PRP matrix, blood is drawn from the patient's arm and concentrated to create a platelet rich solution that floods the injured area with nutrients. With one stem cell injection and one platelet rich plasma injection, spaced out over three to four weeks, the patient will receive the maximum benefits from both procedures. Protocols can be adjusted if the person needs the injections closer together.</p>
    </div>
    <svg class="future-notch" viewBox="0 0 12 330" preserveAspectRatio="none" aria-hidden="true"><path d="M0 0 L12 14 L0 28 Z" fill="#2cb6d1"/></svg>
    <div class="mid-col">
      <h2 class="h">Common <b>contraindications</b></h2>
      <p class="copy">Just like any other healthcare procedure, stem cell therapy does have several contraindications and is inadvisable for patients with specific health conditions. Individuals who have any type of blood borne cancer or have had cancer are normally encouraged not to attempt a stem cell procedure. Patients who are prone to any type of infection or have a depressed immune system should also avoid this type of procedure. The use of Velbrisol can also have a devastating impact on how the procedure works. Patients who use the drug on a regular basis are not good candidates. Individuals who have chronic, recurring medical conditions that affect the body's ability to heal are also not good candidates.</p>
      <h2 class="h">Potential <b>risk factors</b></h2>
      <p class="copy">Stem cell therapy has relatively few risks. The bone marrow cells are harvested from the patient's own tissues so there is minimal risk of rejection. The harvesting process may be somewhat uncomfortable but the doctor can offer medications to help. A mixture of highly concentrated stem cells and growth factors is created and injected directly into the affected area of the joint. Because the procedure is non-invasive, there is very little risk of infection and the healing time is relatively fast.</p>
    </div>
    <div class="mid-left-lower">
      <p class="copy">The patient may experience mild pain and swelling near the injection site for the first few days after the procedure, but this will dissipate rather quickly allowing the person to return to their daily activities.</p>
    </div>
    <div class="photo" role="img" aria-label="Photo of petri dishes with red culture medium"></div>
  </section>

  <!-- Inside: the procedure itself -->
  <section class="panel procedure">
    <div class="photo" role="img" aria-label="Photo of a gloved hand giving an injection into a knee"></div>
    <div class="procedure-bar"><h2 class="h">The <b>procedure</b> itself</h2></div>
    <div class="procedure-body">
      <h3 class="h">How do I <b>prepare</b> for the procedure?</h3>
      <p class="copy">There is very little preparation needed before a stem cell injection procedure. Doctors recommend no anti-inflammatory medications for at least seven to ten days prior. Drink plenty of fluids and make sure you are well rested. During your initial visit, the doctor will ask if you are taking any medications, such as Pondrexa or Velbrisol, so that he can tell you when to discontinue them. The day of the procedure make sure you have someone who can take you home and look after you for the first few hours after the procedure.</p>
      <h3 class="h">What happens when I <b>arrive?</b></h3>
      <p class="copy">The morning of the procedure make sure you are well rested and wearing comfortable clothes. You will be checked in and taken back to a room where the procedure will be performed. The nurse will prep the knee and make sure all of the tools are available. The doctor will begin the harvesting process, drawing blood and stem cells from the marrow of one of your bones. You will be allowed to rest while the matrix is being created, then the solution will be injected into the joint.</p>
      <h3 class="h">What are my <b>limitations</b> after the procedure?</h3>
      <p class="copy">Stem cell procedures do not produce immediate results. It can take anywhere from three to six months or longer for the patient to begin to experience noticeable results. Once the pain begins to subside, the patient should experience renewed mobility and range of motion that allow them to begin to exercise, even if only in modest amounts. The more movement, the stronger the joint. As more cartilage is regenerated, the fewer limitations the patient will experience.</p>
      <p class="copy">Stem cell therapy is not a quick fix. Encouraging proper lifestyle habits, proper nutrition, adequate amounts of fluids and regular exercise will increase the patient's ability to heal faster and more effectively than someone who lives a sedentary lifestyle.</p>
    </div>
  </section>

  <!-- Inside spread, left page -->
  <section class="panel spread-left">
    <div class="intro">
      <h2 class="h">Innovative <b>healing process</b></h2>
      <p class="copy">What started out as a controversial treatment option has turned out to be one of the most unique solutions when it comes to treating joint pain and other health conditions that require the rejuvenation or replacement of certain types of tissues. Individuals who have trouble with their joints due to damage to the bone and cartilage are eager to find solutions that do not involve surgery. Stem cell therapy and the use of amniotic fluids offer solutions that will allow them to begin the healing process and reclaim their lives. Stem cells and platelet rich plasma go hand in hand in helping to regenerate and restore joint structure and function.</p>
      <h2 class="h">Uncovering the <b>benefits</b> of <b>stem cells</b></h2>
      <p class="copy">The study of stem cells has uncovered a myriad of benefits ranging from the relief of migraines to the restoration and rejuvenation of various joints throughout the body. Stem cells are harvested from the patient allowing for a more complete healing in which the body's own tools are given a boost. Because the stem cells are drawn from the person's own body, there is less risk of rejection and the body will begin to restore itself much faster. No foreign substances are used and the healing process that results is much more efficient and complete.</p>
    </div>
    <div class="unique">
      <h2 class="h light">A unique <b>treatment solution</b></h2>
      <p class="copy light">Stem cells offer treatment options and solutions that were unheard of as little as three decades ago. By injecting a matrix made from the body's own "blank" cells, the body is able to regenerate new, healthier tissues that take the place of damaged tissues. Because of how stem cells are formed, they can grow into whatever type of cell is needed, hastening the healing process by rebuilding stronger and healthier tissue. Stem cell therapy gives the body the boost it needs by flooding the area with cells that elicit a healing response.</p>
    </div>
    <div class="photo" role="img" aria-label="Photo of a researcher in safety glasses working with test tubes"></div>
    <div class="effective">
      <h2 class="h">Is the procedure <b>effective?</b></h2>
      <p class="copy">It has been proven that stem cells are capable of regenerating different types of tissues. The procedure's effectiveness, however, will be based on several factors. First and foremost, the extent of damage caused by the injury or disease will determine how effective the procedure will be. If the damage is extensive, the use of stem cells and platelet rich plasma injections may be beneficial, but it will not relieve all of the patient's pain and discomfort. Nerves may be damaged or scar tissue may be present that limits how the bone and cartilage are able to heal. The patient's overall health will also play a vital role. Proper circulation and an abundance of oxygen and nutrients supplied by the bloodstream are imperative if the body's healing responses are expected to regenerate and restore the tissues. The person's willingness to follow the doctor's orders and maintain proper nutrition and physical therapy are also important factors. In the first one or two months, the patient will begin to notice less pain and discomfort. It can take up to six months or longer for the function to improve. The process will be gradual and will continue to improve over time.</p>
    </div>
  </section>

  <!-- Inside spread, right page -->
  <section class="panel spread-right">
    <div class="photo cells" role="img" aria-label="Illustration of round stem cells floating in blue fluid"></div>
    <div class="where">
      <h2 class="h">Where do <b>stem cells</b> come <b>from?</b></h2>
      <p class="copy">Stem cells are no longer drawn from outside sources to be used in joint rejuvenation procedures. The body has an unlimited supply of stem cells that it uses on a regular basis as a way of replacing cells that mature and die off. Doctors have found ways to harvest those cells, as well as growth factors that help to hasten the healing process. Stem cells are produced in the bones, the blood, liver, brain, heart, and soft tissues. Because the body continually produces them, they can be harvested from almost any area at any time without fear of damaging existing tissues.</p>
      <h2 class="h">What types of <b>tissues</b><br>will stem cells <b>restore?</b></h2>
      <p class="copy">Stem cells can be used to regenerate almost any type of tissue, including cartilage and bone. Most people who look to stem cell therapy do so in the hopes that it will relieve their joint pain and allow the joint to function properly. Their rate of effectiveness will be determined by existing factors, such as spurring, severe degeneration, and osteo- or rheumatoid arthritis. Each person's case is unique. The goal of the procedure is to regenerate the damaged tissues and reduce pain and discomfort.</p>
    </div>
    <div class="joints">
      <div class="photo" role="img" aria-label="Illustration of a knee joint with highlighted cartilage"></div>
      <div class="joints-text">
        <h2 class="h">Stem cell <b>treatment<br>options</b> for joints</h2>
        <p class="copy light">Stem cell treatment options can be beneficial in many ways. They are fairly non-invasive in comparison to other types of procedures. The only invasive part is the use of the needle to inject the matrix into the damaged area of the joint. There is practically no down-time and the patient can resume their normal, day-to-day activities within a few hours after the procedure. While it may take a few weeks to notice verifiable results, the addition of a platelet rich plasma injection a few weeks after the initial procedure will help to keep the healing process on track. For knees and other joints, the procedure offers a unique solution that allows the body the opportunity to heal itself without harsh or extremely invasive procedures.</p>
      </div>
    </div>
  </section>

</main>
</body>
</html>
```